Graphic Design Project

I need to create a graphic design, which needs to be editable for me in Powerpoint... I have attached it a draft of it, but I need to be able to change the text of it. I want it to look more professional
Updates

Target Market(s)

Business Executives

Industry/Entity Type

Graphic Design

Requirements
Must have
• Make it look professional; the colors can change; I just need to be able to edit the text in powerpoint or either word

```html
<!DOCTYPE html>
<html lang="en">
<head>
<meta charset="utf-8">
<title>Managing IT Change – Roadmap</title>
<link rel="stylesheet" href="https://fonts.googleapis.com/css2?family=Arimo:wght@400;700&display=swap">
<style>
  :root {
    --canvas: #425619;
    --edge: #2f6f8f;
    --yellow-light: #f9cf4a;
    --yellow-dark: #e39a10;
    --red-light: #e3474d;
    --red-dark: #a80e16;
    --green-light: #9fd150;
    --green-dark: #5f9a1f;
    --brown-light: #bf6a4c;
    --brown-dark: #8a3219;
    --blue-light: #4667ab;
    --blue-dark: #223d7a;
    --ink: #ffffff;
  }
  * { box-sizing: border-box; margin: 0; padding: 0; }
  html, body { width: 1200px; height: 674px; overflow: hidden; }
  body { background: var(--canvas); font-family: "Arimo", Arial, sans-serif; }
  .roadmap { position: relative; width: 1200px; height: 674px; background: var(--canvas); border-top: 3px solid var(--edge); }

  .step {
    position: absolute; width: 228px; height: 137px;
    border-radius: 11px;
    display: flex; align-items: center; justify-content: center; text-align: center;
    color: var(--ink); font-size: 23px; line-height: 1.2;
    text-shadow: 1px 1px 2px rgba(0,0,0,.45);
    box-shadow: 0 3px 5px rgba(0,0,0,.35), inset 0 0 0 2px rgba(0,0,0,.18);
    padding: 0 10px; z-index: 2;
  }
  .step--title { font-size: 29px; }
  .step--yellow { background: radial-gradient(ellipse at 50% 85%, var(--yellow-light), var(--yellow-dark) 85%); }
  .step--red    { background: radial-gradient(ellipse at 50% 85%, var(--red-light), var(--red-dark) 85%); }
  .step--green  { background: radial-gradient(ellipse at 50% 85%, var(--green-light), var(--green-dark) 85%); }
  .step--brown  { background: radial-gradient(ellipse at 50% 85%, var(--brown-light), var(--brown-dark) 85%); }
  .step--blue   { background: radial-gradient(ellipse at 50% 85%, var(--blue-light), var(--blue-dark) 85%); }

  .link { position: absolute; z-index: 1; box-shadow: 0 1px 3px rgba(0,0,0,.3); }
  .link--v { width: 21px; }
  .link--h { height: 21px; }
  .link--yellow { background: var(--yellow-light); }
  .link--red { background: var(--red-light); }
  .link--green { background: var(--green-light); }
  .link--brown { background: var(--brown-light); }
  .link--blue { background: var(--blue-light); }
</style>
</head>
<body>
<main class="roadmap">
  <!-- column one -->
  <div class="step step--yellow step--title" style="left:200px;top:10px">MANAGING</div>
  <div class="step step--red" style="left:200px;top:180px">Maintain IT<br>Operational<br>Excellence<br>CHANGE</div>
  <div class="step step--green" style="left:200px;top:350px">Create Business<br>Value</div>
  <div class="step step--brown" style="left:200px;top:521px">Transform IT<br>Team</div>

  <!-- column two -->
  <div class="step step--green" style="left:503px;top:10px">Service-Minded</div>
  <div class="step step--red" style="left:503px;top:180px">Customer<br>Engagement<br>Model</div>
  <div class="step step--yellow" style="left:503px;top:350px">Market &amp;<br>Communicate<br>Value</div>
  <div class="step step--blue" style="left:503px;top:521px">Master<br>Relationship<br>Management</div>

  <!-- column three -->
  <div class="step step--brown" style="left:806px;top:10px">IT Culture</div>
  <div class="step step--blue" style="left:806px;top:180px">Policy, Process<br>&amp; Methodologies</div>
  <div class="step step--yellow" style="left:806px;top:350px">Meaningful<br>Metrics</div>

  <!-- connectors -->
  <div class="link link--v link--yellow" style="left:237px;top:145px;height:37px"></div>
  <div class="link link--v link--red" style="left:237px;top:315px;height:37px"></div>
  <div class="link link--v link--green" style="left:237px;top:485px;height:38px"></div>
  <div class="link link--h link--brown" style="left:426px;top:545px;width:79px"></div>
  <div class="link link--v link--blue" style="left:540px;top:485px;height:38px"></div>
  <div class="link link--v link--yellow" style="left:540px;top:315px;height:37px"></div>
  <div class="link link--v link--red" style="left:540px;top:145px;height:37px"></div>
  <div class="link link--h link--green" style="left:729px;top:33px;width:79px"></div>
  <div class="link link--v link--brown" style="left:843px;top:145px;height:37px"></div>
  <div class="link link--v link--blue" style="left:843px;top:315px;height:37px"></div>
</main>
</body>
</html>
```